St Louis Electrician Needing a Business Card Design!!

We are a St Louis based electrical contracting firm that needs help designing a business card. We have a logo and I have another image that I would like to incorporate. Open to ideas..Thanks!!

Industry/Entity Type

Business

Requirements
Must have
• there are two downloads...one is the logo and the other is what i was wanting coming off the logo...the light rays. Like the logo with the blue background...Was thinking the whole card would be that color blue.
Should not have
• No lightning bolts

```html
<!DOCTYPE html>
<html lang="en">
<head>
<meta charset="utf-8">
<title>Brightway Electric – Business Card</title>
<link rel="stylesheet" href="https://fonts.googleapis.com/css2?family=Cinzel:wght@400;500&family=Crimson+Text:wght@400&display=swap">
<style>
  :root {
    --stage: #e9ebee;
    --card-blue-light: #1f66c6;
    --card-blue: #1152ac;
    --card-blue-deep: #0b4495;
    --ink-white: #ffffff;
    --ink-soft: rgba(255,255,255,0.55);
    --silver-light: #d7d9dc;
    --silver-mid: #9a9ea4;
    --silver-dark: #5f6369;
    --band-text: #3a3d42;
  }
  * { margin: 0; padding: 0; box-sizing: border-box; }
  html, body {
    width: 1200px; height: 950px; overflow: hidden;
    background: var(--stage);
  }
  .stage {
    width: 1200px; height: 950px;
    display: flex; align-items: center; justify-content: center;
  }
  .business-card {
    position: relative;
    width: 900px; height: 514px;
    border-radius: 4px;
    overflow: hidden;
    background: linear-gradient(160deg, var(--card-blue-light) 0%, var(--card-blue) 45%, var(--card-blue-deep) 100%);
    box-shadow: 0 18px 40px rgba(0,0,0,0.22);
  }
  .card-bands { position: absolute; inset: 0; }
  .company-name {
    position: absolute; left: 78px; top: 300px;
    font-family: "Crimson Text", serif; font-weight: 400;
    font-size: 42px; color: var(--ink-white); letter-spacing: 0.5px;
  }
  .contact-block {
    position: absolute; left: 470px; top: 62px;
    color: var(--ink-white);
  }
  .person-name {
    font-family: "Cinzel", serif; font-weight: 500;
    font-size: 34px; letter-spacing: 1.5px; line-height: 1.1;
  }
  .person-title {
    font-family: "Cinzel", serif; font-weight: 400;
    font-size: 22px; letter-spacing: 1px; margin-top: 2px;
  }
  .divider {
    position: absolute; left: 330px; top: 160px;
    width: 500px; height: 1px; background: var(--ink-soft);
  }
  .contact-details {
    position: absolute; left: 470px; top: 178px;
    font-family: "Crimson Text", serif; font-size: 21px;
    color: var(--ink-white); line-height: 30px; list-style: none;
  }
  .contact-details li { display: flex; align-items: center; gap: 10px; }
  .contact-details .address-line { padding-left: 0; }
  .contact-icon { width: 18px; height: 18px; flex: none; }
  .web-address {
    position: absolute; left: 40px; bottom: 26px;
    font-family: "Crimson Text", serif; font-size: 19px;
    letter-spacing: 1.5px; color: var(--band-text);
  }
</style>
</head>
<body>
<main class="stage">
  <article class="business-card">
    <svg class="card-bands" viewBox="0 0 900 514" width="900" height="514" aria-hidden="true">
      <defs>
        <linearGradient id="silverBand" x1="0" y1="0" x2="1" y2="0.3">
          <stop offset="0" stop-color="var(--silver-dark)"/>
          <stop offset="0.45" stop-color="var(--silver-light)"/>
          <stop offset="0.75" stop-color="var(--silver-mid)"/>
          <stop offset="1" stop-color="var(--silver-dark)"/>
        </linearGradient>
      </defs>
      <path class="white-stripe" fill="var(--ink-white)"
            d="M0,372 C260,460 600,440 900,318 L900,340 C600,458 280,478 0,402 Z"/>
      <path class="silver-band" fill="url(#silverBand)"
            d="M0,402 C280,478 600,458 900,340 L900,514 L0,514 Z"/>
    </svg>

    <div class="company-name">Brightway Electric Inc.</div>

    <header class="contact-block">
      <h1 class="person-name">DANIEL MOORE</h1>
      <p class="person-title">CEO/FOUNDER</p>
    </header>

    <div class="divider"></div>

    <ul class="contact-details">
      <li class="address-line">412 Cedar Hollow Road</li>
      <li class="address-line">Springfield, Ohio 45502</li>
      <li>
        <svg class="contact-icon" viewBox="0 0 24 24" aria-hidden="true"><path fill="#fff" d="M6.6 10.8a15 15 0 0 0 6.6 6.6l2.2-2.2a1 1 0 0 1 1-.25 11.4 11.4 0 0 0 3.6.57 1 1 0 0 1 1 1V20a1 1 0 0 1-1 1A17 17 0 0 1 3 4a1 1 0 0 1 1-1h3.5a1 1 0 0 1 1 1c0 1.25.2 2.45.57 3.6a1 1 0 0 1-.25 1z"/></svg>
        <span>555 210 3841</span>
      </li>
      <li>
        <svg class="contact-icon" viewBox="0 0 24 24" aria-hidden="true"><rect x="6" y="2" width="12" height="20" rx="2" fill="#fff"/><rect x="8" y="5" width="8" height="11" fill="var(--card-blue)"/></svg>
        <span>555 372 9104</span>
      </li>
      <li>
        <svg class="contact-icon" viewBox="0 0 24 24" aria-hidden="true"><rect x="6" y="3" width="12" height="6" fill="#fff"/><rect x="3" y="9" width="18" height="9" rx="1.5" fill="#fff"/><rect x="7" y="14" width="10" height="7" fill="#fff" stroke="var(--card-blue)" stroke-width="1.5"/></svg>
        <span>555 648 2276</span>
      </li>
      <li>
        <svg class="contact-icon" viewBox="0 0 24 24" aria-hidden="true"><rect x="2" y="5" width="20" height="14" rx="1.5" fill="#fff"/><path d="M3 6l9 7 9-7" fill="none" stroke="var(--card-blue)" stroke-width="1.6"/></svg>
        <span>hello@brightwayelectric.com</span>
      </li>
    </ul>

    <p class="web-address">www.brightwayelectric.com</p>
  </article>
</main>
</body>
</html>
```